Home inspection business! professional look attracting customers just by looks. Read must haves

its a new business I started on my own for home inspections I would like something very professional to give to real estate agents and clients, its going to have my license number on it my business phone number my name my website as well etc on the back side it will be servicing areas and also what kind of services I offer I also have a business card from someone else the way I would like mine to be. I will attach my logo

Home Inspection

listed in nice to haves

• phone number - 555 293 8471
• website- hollowpinecheck.com
• license number #2938475610
• my name Gavin keropulis
• picture of my logo and me on the front
• on the back of the card. stating I am servicing All of New York and Long Island
• also services I will offer will be home inspection -mold inspection -lead inspection -radon inspection -Termite Inspection -Infared Scan.
• and also we provide inspections for single family homes condos co-ops town-homes
• and commercial property
• same colors as the logos and also if you recommend fonts to look like the logo not sure up to you

```html
<!DOCTYPE html>
<html lang="en">
<head>
<meta charset="utf-8">
<title>Hollow Pine Inspectors – Business Card</title>
<link rel="stylesheet" href="https://fonts.googleapis.com/css2?family=Open+Sans:wght@400;600;700&display=swap">
<style>
  :root {
    --brand-blue: #1f96d6;
    --ink-dark: #231f20;
    --ink-grey: #5f6062;
    --band-grey: #7a7b7d;
    --paper: #f7f7f8;
    --stage: #e9e9ea;
    --photo-top: #d9d9db;
    --photo-bottom: #9c9da0;
  }
  * { box-sizing: border-box; margin: 0; padding: 0; }
  html, body { width: 1200px; height: 843px; overflow: hidden; }
  body {
    background: var(--stage);
    font-family: "Open Sans", Arial, sans-serif;
    display: flex;
    align-items: center;
    justify-content: center;
    gap: 30px;
  }
  .card {
    position: relative;
    width: 560px;
    height: 320px;
    overflow: hidden;
    box-shadow: 0 6px 18px rgba(0,0,0,.18);
  }

  /* Shared brand lockup: one colour, one weight, two stacked lines */
  .brand {
    position: absolute; display: flex; align-items: center; gap: 10px;
    font-weight: 700; letter-spacing: .5px; white-space: nowrap;
  }
  .brand__dot { border-radius: 50%; flex: none; }
  .brand__name { display: flex; flex-direction: column; line-height: 1.1; }

  /* Front */
  .card--front { background: var(--paper); }
  .portrait {
    position: absolute; left: 62px; top: 62px;
    width: 104px; height: 118px;
    border: 2px solid #3a3a3c;
    border-radius: 4px;
    background: linear-gradient(180deg, var(--photo-top), var(--photo-bottom));
  }
  .holder-name {
    position: absolute; left: 46px; top: 196px;
    color: var(--brand-blue); font-size: 16px; font-weight: 400;
  }
  .card--front .brand { left: 290px; top: 52px; font-size: 20px; color: var(--ink-grey); }
  .card--front .brand__dot { width: 22px; height: 22px; background: var(--brand-blue); }

  .contacts {
    position: absolute; left: 296px; top: 132px;
    list-style: none; color: var(--ink-grey); font-size: 13px;
  }
  .contacts li { display: flex; align-items: center; gap: 14px; height: 26px; }
  .contacts svg { width: 15px; height: 15px; fill: var(--brand-blue); flex: none; }

  .footer-brand {
    position: absolute; left: 24px; top: 242px;
    font-size: 11px; font-weight: 700; color: var(--ink-grey);
  }
  .footer-rule {
    position: absolute; left: 0; right: 0; top: 266px;
    height: 3px; background: var(--brand-blue);
  }
  .footer-band {
    position: absolute; left: 0; right: 0; top: 274px; bottom: 0;
    background: var(--band-grey);
    display: flex; align-items: center; justify-content: flex-end;
    padding-right: 40px;
    color: #fff; font-size: 12px;
  }

  /* Back */
  .card--back { background: var(--ink-dark); }
  .card--back .brand { left: 40px; top: 118px; font-size: 26px; color: #fff; }
  .card--back .brand__dot { width: 28px; height: 28px; background: var(--brand-blue); }
  .services { position: absolute; left: 320px; top: 44px; }
  .services__title {
    color: var(--brand-blue); font-size: 15px; font-weight: 400;
    text-transform: uppercase; margin-bottom: 4px;
  }
  .services__list { list-style: none; color: #fff; font-size: 15px; line-height: 21px; }
  .services__list li { display: flex; align-items: center; gap: 9px; }
  .services__list li::before {
    content: ""; width: 7px; height: 7px; flex: none;
    background:
      linear-gradient(var(--ink-dark), var(--ink-dark)) center/1px 100% no-repeat,
      linear-gradient(var(--ink-dark), var(--ink-dark)) center/100% 1px no-repeat,
      var(--brand-blue);
  }
  .website {
    position: absolute; left: 0; right: 0; bottom: 40px;
    text-align: center; color: var(--brand-blue);
    font-size: 21px; letter-spacing: 7px;
  }
</style>
</head>
<body>

  <section class="card card--front">
    <div class="portrait" role="img" aria-label="Portrait photo of Gavin Keropulis"></div>
    <p class="holder-name">Gavin Keropulis</p>

    <div class="brand">
      <span class="brand__dot"></span>
      <span class="brand__name"><span>HOLLOW PINE</span><span>INSPECTORS</span></span>
    </div>

    <ul class="contacts">
      <li>
        <svg viewBox="0 0 24 24" aria-hidden="true"><path d="M6.6 10.8a15.1 15.1 0 0 0 6.6 6.6l2.2-2.2a1 1 0 0 1 1-.25 11.4 11.4 0 0 0 3.6.57 1 1 0 0 1 1 1V20a1 1 0 0 1-1 1A17 17 0 0 1 3 4a1 1 0 0 1 1-1h3.5a1 1 0 0 1 1 1c0 1.25.2 2.45.57 3.57a1 1 0 0 1-.25 1z"/></svg>
        555 293 8471
      </li>
      <li>
        <svg viewBox="0 0 24 24" aria-hidden="true"><path d="M2 4h20v16H2zm2 2v12h16V6zm2 2h5v5H6zm7 0h5v1.5h-5zm0 3h5v1.5h-5zM6 15h12v1.5H6z"/></svg>
        #2938475610
      </li>
      <li>
        <svg viewBox="0 0 24 24" aria-hidden="true"><path d="M5 2l14 11-6 .8 3.6 6.9-2.6 1.3-3.6-6.9L5 19z"/></svg>
        hollowpinecheck.com
      </li>
    </ul>

    <span class="footer-brand">HOLLOW PINE</span>
    <div class="footer-rule"></div>
    <div class="footer-band">I am servicing All of New York and Long Island</div>
  </section>

  <section class="card card--back">
    <div class="brand">
      <span class="brand__dot"></span>
      <span class="brand__name"><span>HOLLOW PINE</span><span>INSPECTORS</span></span>
    </div>

    <div class="services">
      <h2 class="services__title">Services Provided</h2>
      <ul class="services__list">
        <li>Home Inspection</li>
        <li>Mold Inspection</li>
        <li>Lead Inspection</li>
        <li>Randon Inspection</li>
        <li>Termite Inspection</li>
        <li>Infared Scan</li>
      </ul>
    </div>

    <p class="website">hollowpinecheck.com</p>
  </section>

</body>
</html>
```